Logo Design for "Anvira International School, Jodhpur"

Anvira International School is an international school in Jodhpur. Anvira means "enlightenment" and its literary meaning is "awakening". The word also means "Intelligence" and "Knowledge".

Another meaning in the Buddhist philosophy : The knowledge or understanding of the mechanism by means of which "Liberation" can be attained is also called as "Anvira".

We are already done with our logo design (files attached) and now wish to create font or writing style for the School Name "ANVIRA INTERNATIONAL SCHOOL" so as to make it look very creative or artistic for various stationery, print and presentation purposes.

The first objective is to create the artistic styling of the name, and then take it further for designing of various stationery formats - letter heads, visiting cards, address envelopes, labels, promotional billboards/hoardings, etc.

Thanks to all designers for working on this project.

Unfortunately, it looks like I have not been able to convey my thoughts properly regarding this project.
I wished to have truely creative inputs rather than just manipulations in font styling.  I will appreciate if someone could truely be very creative in generating the font style.  I am looking for something very articulative which positions the style as something created with a vision, or which positions the styling as very high, or something that relates the styling with strong cultural essence or knowledge/intelligence, or something that reflects supremacy of the name.
Request you all to kindly make some truely creative efforts into this.
Regards to all.
Kiran Malvade
Director
Anvira International School
Jodhpur (India)

Reason: Output received is not very interesting.

Reason: Still haven't got the right design where I can say this is the one. Mostly the designs created are manipulations of existing font types only. Will appreciate if someone could be creative.

Reason: I have still not received a design whereby I can say that yes - this is what I need. I have just got some manipulations, nothing truly creative as of now.

My dear friends,

I am still waiting for a good creative design for "Anvira International School".
Have got few options, but nothing is good enough to be finalised. Will appreciate if someone could really offer me something nice and originally created rather than just be manipulations from existing computerized fonts styling.

```html
<!DOCTYPE html>
<html lang="en">
<head>
<meta charset="utf-8">
<title>Anvira International School – Business Card</title>
<link href="https://fonts.googleapis.com/css2?family=Jura:wght@500;700&family=Quicksand:wght@500&display=swap" rel="stylesheet">
<style>
  :root {
    --backdrop: #6e6e6e;
    --backdrop-dark: #555555;
    --card-brown: #5c4a42;
    --card-white: #ffffff;
    --ink-light: #ffffff;
    --shadow: rgba(0, 0, 0, 0.35);
  }
  * { margin: 0; padding: 0; box-sizing: border-box; }
  html, body {
    width: 1200px;
    height: 1000px;
    overflow: hidden;
  }
  body {
    position: relative;
    background: linear-gradient(160deg, var(--backdrop) 0%, var(--backdrop-dark) 100%);
    font-family: "Quicksand", sans-serif;
  }
  .card {
    position: absolute;
    top: 68px;
    width: 480px;
    height: 300px;
    box-shadow: 0 2px 6px var(--shadow);
    overflow: hidden;
  }
  .card--back {
    left: 82px;
    background: var(--card-brown);
    color: var(--ink-light);
  }
  .card--front {
    left: 631px;
    background: var(--card-white);
  }
  .holder {
    position: absolute;
    left: 270px;
    top: 28px;
  }
  .holder__name {
    font-family: "Jura", sans-serif;
    font-weight: 700;
    font-size: 20px;
    letter-spacing: 1px;
    line-height: 1;
    white-space: nowrap;
  }
  .holder__role {
    font-size: 13px;
    margin-top: 5px;
  }
  .contact {
    position: absolute;
    left: 40px;
    top: 190px;
    list-style: none;
    font-size: 14.5px;
    line-height: 20px;
  }
  .contact__item {
    display: flex;
    align-items: center;
    gap: 5px;
    white-space: nowrap;
  }
  .contact__icon {
    width: 11px;
    height: 11px;
    fill: none;
    stroke: var(--ink-light);
    stroke-width: 1.4;
  }
  .contact__item--address { margin-top: 1px; }
  .wordmark {
    position: absolute;
    left: 0;
    right: 0;
    top: 105px;
    display: flex;
    justify-content: center;
    align-items: center;
    gap: 10px;
    font-family: "Quicksand", sans-serif;
    font-weight: 500;
    font-size: 34px;
    color: var(--card-brown);
  }
  .wordmark__dot {
    width: 18px;
    height: 18px;
    border-radius: 50%;
    background: var(--card-brown);
  }
  .school-band {
    position: absolute;
    left: 0;
    right: 0;
    top: 209px;
    height: 34px;
    background: var(--card-brown);
    color: var(--ink-light);
    font-family: "Jura", sans-serif;
    font-weight: 700;
    font-size: 18px;
    letter-spacing: 0.3px;
    line-height: 34px;
    padding-left: 38px;
    white-space: nowrap;
  }
</style>
</head>
<body>

  <section class="card card--back" aria-label="Business card back">
    <div class="holder">
      <p class="holder__name">KIRAN MALVADE</p>
      <p class="holder__role">Director</p>
    </div>
    <ul class="contact">
      <li class="contact__item">
        <svg class="contact__icon" viewBox="0 0 12 12" aria-hidden="true"><path d="M3 1 L5 3.5 L4 5 Q5 7.5 7 8 L8.5 7 L11 9 L9.5 11 Q3 10 1 2.5 Z" fill="#fff" stroke="none"/></svg>
        291-555-0147
      </li>
      <li class="contact__item">
        <svg class="contact__icon" viewBox="0 0 12 12" aria-hidden="true"><rect x="1" y="3" width="10" height="7.5"/><path d="M1 3 L6 7 L11 3"/></svg>
        office@anvira.edu.in
      </li>
      <li class="contact__item">
        <svg class="contact__icon" viewBox="0 0 12 12" aria-hidden="true"><circle cx="6" cy="6" r="5"/><ellipse cx="6" cy="6" rx="2.2" ry="5"/><path d="M1 6 H11"/></svg>
        www.anvira.edu.in
      </li>
      <li class="contact__item contact__item--address">Ratanada Road, Jodhpur, India</li>
    </ul>
  </section>

  <section class="card card--front" aria-label="Business card front">
    <div class="wordmark">
      <span class="wordmark__dot" aria-hidden="true"></span>
      <span class="wordmark__name">Anvira</span>
    </div>
    <p class="school-band">ANVIRA INTERNATIONAL SCHOOL, JODHPUR</p>
  </section>

</body>
</html>
```